Marwick Agency (http://mk.fennoweb-studio.com/)

We are looking for a similar design to what we have, but more professional looking and cleaned up with links and logo that is not so grainy looking. We are an independent insurance agency marketing to personal and commercial clients. We offer all commercial lines markets and all personal lines. We target excavators, landscapers, restaurants, golf courses, contractors. Please look at http://mk.fennoweb-studio.com/ which we had designed but do not like it, it will give you an idea of what we are looking for.

Target Market(s)

Commercial and personal insurance. All business products and all personal (homeowners, auto, antique auto, umbrella)

Industry/Entity Type

It Professional

Logo Text

Knowledge Building Your Assurance

Number of Pages Required

5+ page

Colors
000000
848484
0255a3

```html
<!DOCTYPE html>
<html lang="en">
<head>
<meta charset="utf-8">
<title>Marwick Agency</title>
<link rel="stylesheet" href="https://fonts.googleapis.com/css2?family=Source+Sans+3:wght@400;600;700&display=swap">
<style>
:root{
  --topbar:#3f3f3f;
  --nav-bg:#f5f3f0;
  --brand-blue:#0255a3;
  --button-blue:#2a87d8;
  --text-dark:#222;
  --text-grey:#6f6f6f;
  --nav-grey:#7a7a7a;
  --band-grey:#ebeceb;
  --footer:#414141;
  --footer-text:#6c6c6c;
  --white:#fff;
}
*{box-sizing:border-box;margin:0;padding:0}
html,body{width:1200px;height:1174px;overflow:hidden}
body{font-family:"Source Sans 3",sans-serif;background:var(--white);position:relative;color:var(--text-dark)}
.topbar{position:absolute;left:0;top:0;width:1200px;height:34px;background:var(--topbar);color:#ddd}
.topbar .call{position:absolute;right:221px;top:9px;font-size:12px;display:flex;align-items:center;gap:6px}
.topbar .call strong{font-size:14px;font-weight:600;color:#e8e8e8}
.site-nav{position:absolute;left:0;top:34px;width:1200px;height:50px;background:var(--nav-bg)}
.brand{position:absolute;left:222px;top:12px;font-size:21px;font-weight:700;color:var(--brand-blue);letter-spacing:.5px;text-transform:uppercase}
.menu{list-style:none}
.menu li{position:absolute;top:0;font-size:13px;color:var(--nav-grey);line-height:50px;white-space:nowrap}
.menu li.active{color:var(--text-dark);font-weight:600}
.menu li.active::after{content:"";position:absolute;left:0;right:0;bottom:0;height:2px;background:var(--brand-blue)}
.hero{position:absolute;left:0;top:84px;width:1200px;height:522px;overflow:hidden}
.hero-photo{position:absolute;inset:0;background:
  linear-gradient(180deg,rgba(255,255,255,0) 60%,#fff 100%),
  linear-gradient(100deg,#5a5a58 0%,#7d7b72 30%,#6f7a55 48%,#8a8a86 68%,#9d9d9a 100%)}
.hero-title{position:absolute;left:222px;top:110px;color:var(--white);font-size:31px;font-weight:400;line-height:35px;white-space:nowrap}
.hero-text{position:absolute;left:223px;top:223px;color:var(--white);font-size:15px;line-height:18px;white-space:nowrap}
.hero-actions{position:absolute;left:224px;top:294px;display:flex;gap:18px}
.btn{display:inline-block;height:32px;line-height:32px;padding:0 14px;font-size:12px;font-weight:600;color:var(--white);border-radius:2px}
.btn-primary{background:var(--brand-blue)}
.btn-secondary{background:#9b9b9b}
.about{position:absolute;left:0;top:632px;width:1200px;text-align:center}
.about h2{font-size:21px;font-weight:700;color:var(--brand-blue);letter-spacing:.5px}
.about p{margin:4px auto 0;font-size:13px;line-height:17.5px;color:var(--text-grey);white-space:nowrap}
.services{position:absolute;left:0;top:756px;width:1200px;height:229px;background:var(--band-grey)}
.card{position:absolute;top:36px;width:180px}
.card .photo{height:118px;position:relative}
.card .label{position:absolute;left:0;right:0;bottom:5px;text-align:center;color:var(--white);font-size:15px;font-weight:600}
.quote{margin-top:7px;height:32px;display:flex;color:var(--white)}
.quote .q-text{flex:1;background:var(--button-blue);font-size:17px;font-weight:600;line-height:32px;padding-left:23px}
.quote .q-arrow{width:60px;background:var(--brand-blue);display:flex;align-items:center;justify-content:center}
.footer{position:absolute;left:0;top:1050px;width:1200px;height:124px;background:var(--footer);text-align:center}
.footer .brand-small{margin-top:42px;font-size:19px;font-weight:700;color:#8a8a8a;text-transform:uppercase;letter-spacing:.5px}
.footer small{display:block;font-size:11px;color:var(--footer-text);margin-top:1px}
</style>
</head>
<body>
<header class="topbar">
  <div class="call">Call us today
    <svg width="13" height="13" viewBox="0 0 24 24" aria-hidden="true"><path d="M6.6 10.8a15 15 0 0 0 6.6 6.6l2.2-2.2a1 1 0 0 1 1-.25 11.4 11.4 0 0 0 3.6.57 1 1 0 0 1 1 1V20a1 1 0 0 1-1 1A17 17 0 0 1 3 4a1 1 0 0 1 1-1h3.5a1 1 0 0 1 1 1c0 1.25.2 2.45.57 3.57a1 1 0 0 1-.25 1z" fill="#e07b22"/></svg>
    <strong>1-888-5 (MARWICK)</strong></div>
</header>
<nav class="site-nav">
  <div class="brand">Marwick Agency</div>
  <ul class="menu">
    <li class="active" style="left:487px">Home</li>
    <li style="left:541px">About</li>
    <li style="left:597px">Personal Insurance</li>
    <li style="left:713px">Business Insurance</li>
    <li style="left:832px">Service Centre</li>
    <li style="left:932px">Contacts</li>
  </ul>
</nav>
<section class="hero">
  <div class="hero-photo" role="img" aria-label="Aerial photo of a city square with trees, a café terrace and a busy street, overlaid with a decorative line graphic"></div>
  <h1 class="hero-title">Small Enough To Care,<br>Big Enough To Make<br>A Difference</h1>
  <p class="hero-text">Please find information about our agency, its principles,<br>and the various types of insurance<br>coverages that we provide.</p>
  <div class="hero-actions"><span class="btn btn-primary">Get started now</span><span class="btn btn-secondary">Discover More</span></div>
</section>
<section class="about">
  <h2>ABOUT MARWICK</h2>
  <p>Established in 1950 by the Hollis family, the Marwick Agency was founded on the philosophy of<br>offering personal, professional service. Since then we have grown into a full service agency with a<br>staff of 10 insurance specialist serving over 2,000 individuals and 800 businesses.</p>
</section>
<section class="services">
  <div class="card" style="left:223px">
    <div class="photo" role="img" aria-label="Businessman touching a rising growth chart" style="background:linear-gradient(160deg,#c9c4a0,#4b5566 55%,#1d2230)"><span class="label">Business Insurance</span></div>
    <div class="quote"><span class="q-text">Get Quote</span><span class="q-arrow"><svg width="20" height="14" viewBox="0 0 20 14"><path d="M2 2l5 5-5 5M11 2l5 5-5 5" fill="none" stroke="#fff" stroke-width="3"/></svg></span></div>
  </div>
  <div class="card" style="left:414px">
    <div class="photo" role="img" aria-label="Silver car driving on an open road under a blue sky" style="background:linear-gradient(180deg,#2d62b0,#9bb8d8 45%,#3d3f3a 75%,#1f201c)"><span class="label">Auto Insurance</span></div>
    <div class="quote"><span class="q-text">Get Quote</span><span class="q-arrow"><svg width="20" height="14" viewBox="0 0 20 14"><path d="M2 2l5 5-5 5M11 2l5 5-5 5" fill="none" stroke="#fff" stroke-width="3"/></svg></span></div>
  </div>
  <div class="card" style="left:606px">
    <div class="photo" role="img" aria-label="Business people holding black umbrellas in the rain" style="background:linear-gradient(180deg,#4a6c7a,#2a3a42 60%,#111)"><span class="label">Life Insurance</span></div>
    <div class="quote"><span class="q-text">Get Quote</span><span class="q-arrow"><svg width="20" height="14" viewBox="0 0 20 14"><path d="M2 2l5 5-5 5M11 2l5 5-5 5" fill="none" stroke="#fff" stroke-width="3"/></svg></span></div>
  </div>
  <div class="card" style="left:796px">
    <div class="photo" role="img" aria-label="Hand holding a small model house" style="background:linear-gradient(180deg,#9a9a96,#c7c3bd 50%,#b98f78 80%,#6b84b8)"><span class="label">Home Insurance</span></div>
    <div class="quote"><span class="q-text">Get Quote</span><span class="q-arrow"><svg width="20" height="14" viewBox="0 0 20 14"><path d="M2 2l5 5-5 5M11 2l5 5-5 5" fill="none" stroke="#fff" stroke-width="3"/></svg></span></div>
  </div>
</section>
<footer class="footer">
  <div class="brand-small">Marwick Agency</div>
  <small>Copyright 2015. All rights reserved.</small>
</footer>
</body>
</html>
```